FinTech company looking to revamp and expand client-facing interface for our financial models

Halvern Ledgerworks currently has a very simple website that allows clients to interact with our financial models. We are looking to completely redesign the current site and add several extra pages to provide extra functionality. We want the design to have a modern, slick feel, that will work on both a desktop or a tablet. It should be straightforward for clients to move between different pages at any time, and clear from the layout how to interact with the more advanced features. We have included screenshots of existing pages in the attached design brief, as well as sketches of the functionality required by the new pages, but can't provide a direct link to the current site.
Target Market(s)
Professional investors that will be paying to access the interface
Industry/Entity Type
Finance
Number of Pages Required
4 page
Colors
Designer to choose colors to be used in the design.
Look and feel
Each slider illustrates characteristics of the customer's brand and the style your logo design should communicate.

```html
<!DOCTYPE html>
<html lang="en">
<head>
<meta charset="utf-8">
<title>Halvern Ledgerworks – Portfolio</title>
<link href="https://fonts.googleapis.com/css2?family=Open+Sans:wght@400;600;700&display=swap" rel="stylesheet">
<style>
:root{
  --teal-dark:#006766;
  --teal:#2aa899;
  --row-alt:#e3f2ef;
  --ink:#1a1a1a;
  --black:#1b1b1b;
  --navy:#06376e;
  --green:#1fae1f;
  --bar-green:#00cc00;
  --red:#b30b0b;
  --bar-red:#ff0000;
  --minus:#a51d1d;
  --bg:#efefef;
  --line:#dcdcdc;
  --blue-dot:#3a6fae;
  --olive-dot:#b8b838;
}
*{box-sizing:border-box;margin:0;padding:0}
html,body{width:1200px;height:1149px;overflow:hidden}
body{font-family:"Open Sans",sans-serif;color:var(--ink);background:linear-gradient(#e4e4e4,#f5f5f5 300px,#f7f7f7);position:relative}
.topbar{position:absolute;left:0;top:0;width:1200px;height:55px;background:#fff;box-shadow:0 4px 10px rgba(0,0,0,.12)}
.brand{position:absolute;left:67px;top:0;line-height:55px;font-weight:700;font-size:18px;letter-spacing:.3px}
.nav-item{position:absolute;top:0;height:55px;border-left:1px solid #e2e2e2;display:flex;align-items:center;justify-content:center;gap:8px;font-weight:700;font-size:13px}
.nav-item svg{width:22px;height:22px}
.nav-item.active{background:var(--teal);color:#fff;border-left:none;font-weight:600}
.panel{position:absolute;background:#fff;box-shadow:0 3px 8px rgba(0,0,0,.15)}
.members{left:65px;top:92px;width:517px;height:480px;border-radius:4px 4px 0 0;overflow:hidden}
.members .title{height:46px;background:var(--black);color:#fff;font-weight:600;font-size:16px;text-align:center;line-height:46px}
.members .cols{display:flex;height:47px;background:var(--teal-dark);color:#fff;font-weight:600;font-size:15px;line-height:47px;text-align:center}
.members .cols div:first-child{width:240px;border-right:1px solid #2c8c89}
.members .cols div:last-child{width:277px}
.members .row{display:flex;height:64.5px;width:480px;align-items:center;font-size:16px}
.members .row:nth-child(even){background:var(--row-alt)}
.members .name{width:240px;display:flex;align-items:center;gap:14px;padding-left:47px;border-right:1px solid #e7eeee;height:100%}
.members .size{width:240px;text-align:center}
.scrolltrack{position:absolute;left:480px;top:93px;width:37px;height:387px;background:#d6d6d6}
.scrolltrack .rail{position:absolute;left:10px;top:24px;width:18px;height:342px;background:#fff;border-radius:9px;border:1px solid #ccc}
.scrolltrack .thumb{position:absolute;left:10px;top:24px;width:18px;height:68px;background:#8c8c8c;border-radius:9px}
.sens{left:618px;top:92px;width:517px;height:323px;border-radius:4px;overflow:hidden}
.sens .title{height:65px;background:var(--teal-dark);color:#fff;font-weight:600;font-size:16px;text-align:center;line-height:65px}
.sens .row{height:64.5px;position:relative;display:flex;align-items:center;font-size:16px;padding-left:26px}
.sens .row:nth-child(odd){background:var(--row-alt)}
.gauge{position:absolute;left:199px;top:9px;width:297px;height:47px;background:#e3e3e3;padding:7px 10px}
.gauge .box{position:relative;width:100%;height:100%;background:#fff;border:1px solid #cfcfcf}
.gauge .tick{position:absolute;top:0;bottom:0;width:1px;background:#e4e4e4}
.gauge .axis{position:absolute;left:138px;top:-8px;bottom:-8px;width:2px;background:#777}
.gauge .bar{position:absolute;top:0;bottom:0}
.gauge .val{position:absolute;top:0;line-height:31px;font-size:16px;letter-spacing:-.5px}
.btn{position:absolute;top:591px;height:37px;border-radius:3px;color:#fff;font-weight:700;font-size:15px;display:flex;align-items:center;justify-content:center;gap:8px;letter-spacing:.1px}
.btn svg{width:20px;height:20px}
.btn.add{left:65px;width:164px;background:var(--navy)}
.btn.save{left:237px;width:177px;background:var(--green)}
.btn.clear{left:424px;width:131px;background:var(--red)}
.chartcard{left:65px;top:683px;width:1070px;height:392px;border-radius:4px;overflow:hidden}
.chartcard .tabbar{position:absolute;left:0;top:0;width:100%;height:79px;background:#efefef}
.tab{position:absolute;top:46px;width:83px;height:33px;background:#fff;text-align:center;line-height:35px;font-size:16px;font-weight:600;color:#333}
.tab.active{top:37px;height:42px;background:#cfcfcf;line-height:48px;color:#555}
.chartcard svg.plot{position:absolute;left:0;top:79px}
</style>
</head>
<body>
<header class="topbar">
  <div class="brand">HALVERN</div>
  <div class="nav-item" style="left:180px;width:84px">250D</div>
  <div class="nav-item" style="left:264px;width:83px">83D</div>
  <div class="nav-item" style="left:347px;width:83px">42D</div>
  <div class="nav-item" style="left:430px;width:125px"></div>
  <div class="nav-item" style="left:555px;width:129px">
    <svg viewBox="0 0 24 24"><path d="M2 12 12 3l10 9h-3v9h-5v-6h-4v6H5v-9z" fill="#111"/></svg>MODELS</div>
  <div class="nav-item" style="left:684px;width:163px">
    <svg viewBox="0 0 24 24" fill="#222"><circle cx="12" cy="12" r="3"/><g><circle cx="12" cy="3" r="1.6"/><circle cx="12" cy="21" r="1.6"/><circle cx="3" cy="12" r="1.6"/><circle cx="21" cy="12" r="1.6"/><circle cx="5.6" cy="5.6" r="1.6"/><circle cx="18.4" cy="18.4" r="1.6"/><circle cx="5.6" cy="18.4" r="1.6"/><circle cx="18.4" cy="5.6" r="1.6"/><circle cx="12" cy="7" r="1"/><circle cx="12" cy="17" r="1"/><circle cx="7" cy="12" r="1"/><circle cx="17" cy="12" r="1"/></g></svg>SENSITIVITIES</div>
  <div class="nav-item active" style="left:847px;width:149px">
    <svg viewBox="0 0 24 24" fill="none" stroke="#fff" stroke-width="1.6"><circle cx="6.5" cy="6.5" r="4"/><circle cx="17.5" cy="6.5" r="4"/><circle cx="6.5" cy="17.5" r="4"/><circle cx="17.5" cy="17.5" r="4"/></svg>PORTFOLIO</div>
  <div class="nav-item" style="left:996px;width:139px;border-right:1px solid #e2e2e2">
    <svg viewBox="0 0 24 24" fill="none" stroke="#111" stroke-width="1.8"><rect x="2" y="3" width="20" height="17"/><path d="M5 16l4-6 3 4 3-7 4 9"/></svg>BACKTEST</div>
</header>

<section class="panel members">
  <div class="title">Current Members</div>
  <div class="cols"><div>Members Name</div><div>Size</div></div>
  <div class="rows">
    <div class="row"><div class="name"><svg width="24" height="24" viewBox="0 0 24 24"><circle cx="12" cy="12" r="10" fill="none" stroke="var(--minus)" stroke-width="2"/><path d="M7 12h10" stroke="var(--minus)" stroke-width="2"/></svg>Member 1</div><div class="size">0.2</div></div>
    <div class="row"><div class="name"><svg width="24" height="24" viewBox="0 0 24 24"><circle cx="12" cy="12" r="10" fill="none" stroke="var(--minus)" stroke-width="2"/><path d="M7 12h10" stroke="var(--minus)" stroke-width="2"/></svg>Member 2</div><div class="size">0.5</div></div>
    <div class="row"><div class="name"><svg width="24" height="24" viewBox="0 0 24 24"><circle cx="12" cy="12" r="10" fill="none" stroke="var(--minus)" stroke-width="2"/><path d="M7 12h10" stroke="var(--minus)" stroke-width="2"/></svg>Member 3</div><div class="size">-0.3</div></div>
    <div class="row"><div class="name"><svg width="24" height="24" viewBox="0 0 24 24"><circle cx="12" cy="12" r="10" fill="none" stroke="var(--minus)" stroke-width="2"/><path d="M7 12h10" stroke="var(--minus)" stroke-width="2"/></svg>Member 4</div><div class="size">0.2</div></div>
    <div class="row"><div class="name"><svg width="24" height="24" viewBox="0 0 24 24"><circle cx="12" cy="12" r="10" fill="none" stroke="var(--minus)" stroke-width="2"/><path d="M7 12h10" stroke="var(--minus)" stroke-width="2"/></svg>Member 5</div><div class="size">0.5</div></div>
    <div class="row"><div class="name"><svg width="24" height="24" viewBox="0 0 24 24"><circle cx="12" cy="12" r="10" fill="none" stroke="var(--minus)" stroke-width="2"/><path d="M7 12h10" stroke="var(--minus)" stroke-width="2"/></svg>Member 6</div><div class="size">-0.3</div></div>
  </div>
  <div class="scrolltrack"><div class="rail"></div><div class="thumb"></div></div>
</section>

<section class="panel sens">
  <div class="title">Sensitivities</div>
  <div class="row">A-Lorem ipsum dolor
    <div class="gauge"><div class="box"><div class="tick" style="left:69px"></div><div class="tick" style="left:207px"></div><div class="bar" style="left:139px;width:62px;background:var(--bar-green)"></div><div class="axis"></div><div class="val" style="left:212px">0.9</div></div></div></div>
  <div class="row">B-Lorem ipsum dolor
    <div class="gauge"><div class="box"><div class="tick" style="left:69px"></div><div class="tick" style="left:207px"></div><div class="bar" style="left:139px;width:49px;background:var(--bar-green)"></div><div class="axis"></div><div class="val" style="left:198px">0.7</div></div></div></div>
  <div class="row">C-Lorem ipsum dolor
    <div class="gauge"><div class="box"><div class="tick" style="left:69px"></div><div class="tick" style="left:207px"></div><div class="bar" style="left:101px;width:38px;background:var(--bar-red)"></div><div class="axis"></div><div class="val" style="left:66px">-0.6</div></div></div></div>
  <div class="row">D-Lorem ipsum dolor
    <div class="gauge"><div class="box"><div class="tick" style="left:69px"></div><div class="tick" style="left:207px"></div><div class="bar" style="left:121px;width:18px;background:var(--bar-red)"></div><div class="axis"></div><div class="val" style="left:86px">-0.3</div></div></div></div>
</section>

<div class="btn add"><svg viewBox="0 0 24 24" fill="none" stroke="#fff" stroke-width="1.8"><circle cx="12" cy="12" r="10"/><path d="M12 7v10M7 12h10"/></svg>ADD MEMBERS</div>
<div class="btn save"><svg viewBox="0 0 24 24" fill="none" stroke="#fff" stroke-width="3.5"><path d="M3 12l6 6L21 5"/></svg>SAVE PORTFOLIO</div>
<div class="btn clear"><svg viewBox="0 0 24 24" fill="none" stroke="#fff" stroke-width="3.5"><path d="M4 4l16 16M20 4 4 20"/></svg>CLEAR ALL</div>

<section class="panel chartcard">
  <div class="tabbar">
    <div class="tab" style="left:51px">#1</div>
    <div class="tab" style="left:139px">#2</div>
    <div class="tab" style="left:226px">#3</div>
    <div class="tab active" style="left:314px">#4</div>
  </div>
  <svg class="plot" width="1070" height="313" viewBox="70 825 1160 340" role="img" aria-label="Scatter chart of member scores from Jul 2018 to Jul 2019">
    <g stroke="#ececec" stroke-width="1">
      <path d="M182 887H1075M182 925H1075M182 962H1075M182 1000H1075M182 1037H1075"/>
      <path d="M182 875V1075M325 875V1075M465 875V1075M605 875V1075M742 875V1075M882 875V1075M1022 875V1075"/>
    </g>
    <path d="M150 1075H1077" stroke="#888" stroke-width="1.3"/>
    <g font-family="Open Sans, sans-serif" font-size="11.5" fill="#555" text-anchor="end">
      <text x="151" y="891">100</text><text x="151" y="929">80</text><text x="151" y="966">60</text><text x="151" y="1004">40</text><text x="151" y="1041">20</text><text x="151" y="1079">0</text>
    </g>
    <g font-family="Open Sans, sans-serif" font-size="11.5" fill="#555" text-anchor="middle">
      <text x="182" y="1100">Jul 2018</text><text x="325" y="1100">Sep 2018</text><text x="465" y="1100">Nov 2018</text><text x="605" y="1100">Jan 2019</text><text x="742" y="1100">Mar 2019</text><text x="882" y="1100">May 2019</text><text x="1022" y="1100">Jul 2019</text>
    </g>
    <g fill="none" stroke-linecap="round" stroke-width="7">
      <path stroke="var(--olive-dot)" d="M202 887h0M208 888h0M214 887h0M220 888h0M226 887h0M232 887h0M238 888h0M244 887h0M250 887h0M256 888h0M262 887h0M268 887h0M274 888h0M280 887h0M285 895h0M290 905h0M298 903h0M305 893h0M312 890h0M320 895h0M328 893h0M334 900h0M336 955h0M340 985h0M345 1000h0M350 967h0M352 988h0M358 1003h0M365 990h0M370 980h0M374 995h0M378 992h0M380 948h0M385 953h0M390 930h0M395 918h0M398 915h0M402 888h0M408 893h0M410 945h0M413 965h0M416 960h0M420 985h0M425 975h0M430 970h0M433 1050h0M438 1040h0M442 1045h0M448 1025h0M452 1030h0M456 1035h0M460 1018h0M465 1060h0M470 1065h0M475 1068h0M480 1060h0M485 1055h0M490 1050h0M495 1040h0M500 1035h0M510 1008h0M515 1030h0M520 1010h0M525 1015h0M528 970h0M533 962h0M540 965h0M542 890h0M550 888h0M558 888h0M565 895h0M572 890h0M576 1060h0M580 1065h0M590 1060h0M595 1058h0M600 1050h0M605 1055h0M610 1045h0M615 1055h0M620 1050h0M625 1060h0M630 1058h0M635 1055h0M640 1050h0M645 1040h0M652 1022h0M656 1022h0M655 952h0M668 952h0M660 990h0M660 1002h0M672 905h0M672 915h0M686 910h0M690 965h0M694 1030h0M700 1033h0M702 1045h0M705 910h0M708 945h0M710 930h0M714 945h0M718 945h0M720 990h0M720 900h0M728 893h0M735 905h0M738 910h0M742 897h0M750 893h0M752 905h0M756 900h0"/>
      <line x1="760" y1="890" x2="1000" y2="890" stroke="var(--olive-dot)" stroke-dasharray="0 8"/>
      <path stroke="var(--blue-dot)" d="M205 900h0M210 893h0M215 900h0M220 893h0M221 900h0M203 953h0M223 969h0M255 964h0M268 967h0M225 1000h0M233 997h0M235 1015h0M238 1030h0M240 1020h0M248 1008h0M250 1025h0M258 990h0M262 993h0M268 988h0M272 995h0M276 1028h0M280 1020h0M285 1024h0M290 1002h0M296 998h0M300 1025h0M303 1018h0M306 1030h0M310 1022h0M315 1028h0M320 1023h0M325 1030h0M333 1035h0M338 1050h0M344 1055h0M350 1048h0M355 1052h0M360 1055h0M365 1047h0M370 1050h0M376 1048h0M380 1030h0M385 1025h0M390 1020h0M395 1018h0M400 1025h0M405 1030h0M410 1040h0M415 1020h0M420 1035h0M425 1045h0M430 1030h0M435 1070h0M440 1060h0M445 1070h0M450 1055h0M455 1050h0M462 1055h0M463 945h0M468 918h0M472 915h0M476 912h0M480 902h0M478 922h0M485 910h0M488 925h0M492 924h0M496 1020h0M500 1040h0M505 1050h0M510 1030h0M515 1026h0M520 1010h0M525 1040h0M532 993h0M538 994h0M542 910h0M545 905h0M550 895h0M556 892h0M560 898h0M565 902h0M570 900h0M573 905h0"/>
      <line x1="590" y1="887" x2="1026" y2="887" stroke="var(--blue-dot)" stroke-dasharray="0 7"/>
      <path stroke="#4a9a3a" d="M1000 1071h0M1005 1071h0M1010 1071h0"/>
    </g>
    <text x="1132" y="890" font-family="Georgia, serif" font-size="11" fill="#444">Names</text>
    <g>
      <circle cx="1114" cy="886" r="3.5" fill="#8fb3d6"/><circle cx="1114" cy="905" r="3.5" fill="#f0a060"/><circle cx="1114" cy="923" r="3.5" fill="#3a9a3a"/><circle cx="1114" cy="942" r="3.5" fill="#e07070"/><circle cx="1114" cy="960" r="3.5" fill="#b090d0"/><circle cx="1114" cy="979" r="3.5" fill="#a08a80"/><circle cx="1114" cy="998" r="3.5" fill="#e0a0d0"/><circle cx="1114" cy="1016" r="3.5" fill="#aaaaaa"/><circle cx="1114" cy="1035" r="3.5" fill="#b8b838"/><circle cx="1114" cy="1054" r="3.5" fill="#80d0e0"/><circle cx="1114" cy="1073" r="3.5" fill="#3a6fae"/>
    </g>
  </svg>
</section>
</body>
</html>
```